Silver lantern Tarot

I need a logo for my business cards for my tarot reading business. I want the cards to be representative of the (linden/Crane) tarot cards, similar style/design & feel to these cards. It needs to feature a feather & a reference to birds. Can I please have designs featuring a black bird & a white bird intersecting or relating to each other
Please see image below & use as inspiration I really love this image
Contact Information for Business Card
Silver Lantern Tarot
Email silverlanterntarot@postvale.com
Phone Marisa 0437291604 or Denise 0437 526 083

```html
<!DOCTYPE html>
<html lang="en">
<head>
<meta charset="utf-8">
<title>Silver Lantern Tarot – Business Card</title>
<link href="https://fonts.googleapis.com/css2?family=Arimo:wght@400&display=swap" rel="stylesheet">
<style>
  :root {
    --page-bg: #d8d3cb;
    --card-black: #000000;
    --ink-white: #f4f4f4;
    --rule-grey: #5a5a5a;
    --silver-light: #e6e6e6;
    --silver-dark: #6b6b6b;
  }
  * { margin: 0; padding: 0; box-sizing: border-box; }
  html, body {
    width: 1200px;
    height: 1200px;
    overflow: hidden;
    background: var(--page-bg);
    font-family: "Arimo", Arial, sans-serif;
  }
  .sheet {
    width: 1200px;
    height: 1200px;
    display: flex;
    flex-direction: column;
    align-items: center;
    justify-content: center;
    gap: 70px;
  }
  .card {
    position: relative;
    width: 840px;
    height: 480px;
    background: var(--card-black);
    color: var(--ink-white);
    box-shadow: 0 6px 18px rgba(0,0,0,0.25);
    overflow: hidden;
  }
  .brand-name {
    font-variant: small-caps;
    letter-spacing: 0.04em;
    font-weight: 400;
  }

  /* Front */
  .card-front .brand-mark {
    position: absolute;
    left: 150px;
    top: 110px;
    display: flex;
    align-items: center;
    gap: 22px;
  }
  .card-front .brand-mark .mark-circle {
    width: 150px;
    height: 150px;
    border-radius: 50%;
    background: radial-gradient(circle at 40% 35%, var(--silver-light), var(--silver-dark));
  }
  .card-front .brand-name {
    position: absolute;
    left: 320px;
    bottom: 90px;
    font-size: 40px;
  }

  /* Back */
  .card-back .brand-name {
    position: absolute;
    left: 70px;
    top: 60px;
    font-size: 26px;
  }
  .card-back .divider {
    position: absolute;
    left: 250px;
    right: 250px;
    top: 300px;
    height: 1px;
    background: var(--rule-grey);
  }
  .contact-list {
    position: absolute;
    right: 60px;
    top: 110px;
    list-style: none;
    font-size: 26px;
    line-height: 1.55;
  }
  .contact-list li {
    display: flex;
    align-items: center;
    gap: 12px;
  }
  .contact-list .phone-icon {
    width: 24px;
    height: 24px;
    flex: none;
  }
</style>
</head>
<body>
<main class="sheet">

  <section class="card card-front" aria-label="Card front">
    <div class="brand-mark">
      <span class="mark-circle" aria-hidden="true"></span>
    </div>
    <h1 class="brand-name">Silver Lantern Tarot</h1>
  </section>

  <section class="card card-back" aria-label="Card back">
    <p class="brand-name">Silver Lantern Tarot</p>
    <ul class="contact-list">
      <li>
        <svg class="phone-icon" viewBox="0 0 24 24" aria-hidden="true">
          <circle cx="12" cy="12" r="10.5" fill="none" stroke="#f4f4f4" stroke-width="1.5"/>
          <path d="M8.2 6.8l2 2.2-1.1 1.5c.7 1.6 1.8 2.8 3.4 3.6l1.5-1.1 2.2 2-1 1.6c-3.8-.4-7.2-3.8-7.6-7.6z" fill="#f4f4f4"/>
        </svg>
        <span>Marisa 0437 291 604</span>
      </li>
      <li>
        <svg class="phone-icon" viewBox="0 0 24 24" aria-hidden="true">
          <circle cx="12" cy="12" r="10.5" fill="none" stroke="#f4f4f4" stroke-width="1.5"/>
          <path d="M8.2 6.8l2 2.2-1.1 1.5c.7 1.6 1.8 2.8 3.4 3.6l1.5-1.1 2.2 2-1 1.6c-3.8-.4-7.2-3.8-7.6-7.6z" fill="#f4f4f4"/>
        </svg>
        <span>Denise 0437 526 083</span>
      </li>
      <li><span>silverlanterntarot@postvale.com</span></li>
    </ul>
    <div class="divider" aria-hidden="true"></div>
  </section>

</main>
</body>
</html>
```